Make attractive Packaging label for NUT BUTTERS jars

We at Briarwood Pantry are launching our own line of NUT BUTTERS. We will be serving them in GLASS JARS ready packaged. I need attractive luxurious design for glass jar and should be designed ready to print.
I have attached glass jar pictures and measurement sheet.
My company logo has been attached. Also company details can be found on our facebook page.
product will be

ALMOND BUTTER
CASHEW BUTTER
PEANUT BUTTER
HAZELNUT BUTTER.

Industry/Entity Type

Retail

```html
<!DOCTYPE html>
<html lang="en">
<head>
<meta charset="UTF-8">
<title>Briarwood Pantry Almond Butter Label</title>
<link href="https://fonts.googleapis.com/css2?family=Roboto+Condensed:wght@300;700&display=swap" rel="stylesheet">
<style>
  :root {
    --page: #ffffff;
    --wood-dark: #6e3512;
    --wood-mid: #9a5020;
    --wood-light: #c27634;
    --panel: #3a2222;
    --panel-edge: #2a1616;
    --gold: #d9b66c;
    --gold-light: #f3dc9c;
    --gold-deep: #b08440;
    --white: #f7f5f2;
    --badge: #d9243a;
    --almond-shell: #c98b55;
    --almond-light: #e9c79c;
    --side-text: #5a2c10;
  }
  * { margin: 0; padding: 0; box-sizing: border-box; }
  html, body { width: 1200px; height: 1116px; overflow: hidden; background: var(--page); }
  .canvas { position: relative; width: 1200px; height: 1116px; background: var(--page); }

  .label {
    position: absolute; left: 212px; top: 328px; width: 768px; height: 668px;
    background: linear-gradient(90deg, var(--wood-dark) 0%, var(--wood-mid) 30%, var(--wood-light) 60%, var(--wood-mid) 100%);
    overflow: hidden;
    font-family: "Roboto Condensed", sans-serif;
  }

  .front-panel {
    position: absolute; left: 96px; top: 24px; width: 564px; height: 528px;
    background: linear-gradient(90deg, var(--panel-edge) 0%, var(--panel) 50%, #4a2e2c 100%);
  }

  .brand-name {
    position: absolute; left: 0; width: 564px; top: 28px;
    text-align: center; font-weight: 700; font-size: 46px; line-height: 1;
    color: var(--gold); white-space: nowrap;
  }

  .product-title { position: absolute; left: 0; top: 0; width: 564px; height: 528px; }
  .product-title text { font-family: "Roboto Condensed", sans-serif; font-weight: 700; font-size: 197px; }
  .product-word--nut { fill: var(--white); }

  .art-almond {
    position: absolute;
    background: linear-gradient(135deg, var(--almond-light), var(--almond-shell));
    border-radius: 50%;
  }
  .art-almond--broken { left: 12px; top: 128px; width: 142px; height: 62px; transform: rotate(8deg); }
  .art-almond--pair { left: 448px; top: 86px; width: 96px; height: 86px; }

  .almond-pile {
    position: absolute; left: 40px; top: 564px; width: 728px; height: 76px;
    background: linear-gradient(180deg, var(--almond-light) 0%, var(--almond-shell) 70%, var(--wood-mid) 100%);
    border-radius: 38px 38px 0 0;
  }

  .badge-natural {
    position: absolute; left: 308px; top: 584px; width: 256px; height: 56px;
    background: var(--badge);
    font-weight: 700; font-size: 34px;
    color: var(--white); display: flex; align-items: center; justify-content: center;
  }

  .side-copy {
    position: absolute; left: 680px; top: 136px; height: 400px; width: 60px;
    writing-mode: vertical-rl; transform: rotate(180deg);
    font-weight: 300; font-size: 13px; line-height: 19px; letter-spacing: 1.2px;
    color: var(--side-text); text-transform: uppercase; white-space: nowrap;
  }
</style>
</head>
<body>
<main class="canvas">
  <section class="label">
    <div class="front-panel">
      <div class="brand-name">Briarwood Pantry</div>
      <div class="art-almond art-almond--broken" role="img" aria-label="Whole and cracked almond illustration"></div>
      <div class="art-almond art-almond--pair" role="img" aria-label="Two whole almonds illustration"></div>
      <svg class="product-title" viewBox="0 0 564 528" aria-label="Almond Butter">
        <defs>
          <linearGradient id="butterGold" x1="0" y1="0" x2="0" y2="1">
            <stop offset="0" stop-color="#f3dc9c"/>
            <stop offset="0.55" stop-color="#d9b66c"/>
            <stop offset="1" stop-color="#b08440"/>
          </linearGradient>
        </defs>
        <text class="product-word--nut" x="24" y="340" textLength="508" lengthAdjust="spacingAndGlyphs">ALMOND</text>
        <text x="28" y="500" textLength="512" lengthAdjust="spacingAndGlyphs" fill="url(#butterGold)">BUTTER</text>
      </svg>
    </div>
    <div class="almond-pile" role="img" aria-label="Row of whole almonds along the bottom of the label"></div>
    <div class="badge-natural">100% NATURAL</div>
    <p class="side-copy">A delicious spread on toasts, for baking, making<br>sauces etc. No hydrogenated oil. No preservatives.<br>Contains no sugar (unsweetened). - Simply good food</p>
  </section>
</main>
</body>
</html>
```